Harbinger Postcard Design

We need postcard designs for a new company based in Maryland called "Harbinger". We provide security guard services and we provide training for security guards. We would like two different cards, one for individuals who need training to become security guards through our training academy, and one targeted at businesses that are looking to hire security guards through our security agency. We are looking to project an image of strength, stability, trustworthiness and confidence.

Target Market(s)

Businesses that typically use security guard services, such as property management companies, restaurants, construction companies, etc.

Industry/Entity Type

Security

Requirements
Must have
• The card should be professional. It needs to grab the reader's attention right away.

```html
<!DOCTYPE html>
<html lang="en">
<head>
<meta charset="utf-8">
<title>Harbinger Security Postcard</title>
<link href="https://fonts.googleapis.com/css2?family=Archivo+Black&family=Lato:wght@700;900&family=Oswald:wght@600&display=swap" rel="stylesheet">
<style>
  :root {
    --brand-blue: #3f4fa3;
    --sky-text: #8fd3f0;
    --address-blue: #86c9ec;
    --ink: #2e2e33;
    --band-black: #050505;
    --paper: #ffffff;
    --arrow-blue: #3d4fa8;
  }
  * { margin: 0; padding: 0; box-sizing: border-box; }
  html, body { width: 1200px; height: 900px; overflow: hidden; background: #ffffff; }
  .postcard {
    position: relative;
    width: 1200px;
    height: 900px;
    overflow: hidden;
    background: var(--paper);
    font-family: "Lato", Arial, sans-serif;
  }
  .postcard-backdrop { position: absolute; inset: 0; }
  .tagline {
    position: absolute;
    top: 84px;
    left: 0;
    width: 1200px;
    text-align: center;
    font-family: "Oswald", "Arial Narrow", sans-serif;
    font-weight: 600;
    font-size: 29px;
    letter-spacing: 0.3px;
    color: var(--sky-text);
    text-transform: uppercase;
  }
  .services-tab {
    position: absolute;
    top: 164px;
    left: 42px;
    width: 498px;
    height: 76px;
    background: var(--brand-blue);
    border-radius: 0 0 28px 28px;
    color: var(--paper);
    font-family: "Archivo Black", Arial, sans-serif;
    font-size: 48px;
    line-height: 78px;
    text-align: center;
  }
  .service-list {
    position: absolute;
    top: 262px;
    left: 44px;
    width: 560px;
    list-style: none;
    color: var(--ink);
    font-weight: 700;
    font-size: 31px;
    line-height: 36px;
  }
  .service-list li {
    position: relative;
    padding-left: 40px;
  }
  .service-list li::before {
    content: "\2192";
    position: absolute;
    left: 0;
    top: -2px;
    color: var(--arrow-blue);
    font-weight: 900;
  }
  .guard-photo {
    position: absolute;
    top: 150px;
    left: 598px;
    width: 570px;
    height: 646px;
  }
  .brand-block {
    position: absolute;
    left: 42px;
    top: 586px;
    width: 248px;
    height: 224px;
    background: var(--band-black);
    display: flex;
    align-items: center;
    justify-content: center;
    gap: 10px;
  }
  .brand-dot {
    width: 20px;
    height: 20px;
    border-radius: 50%;
    background: var(--sky-text);
  }
  .brand-name {
    color: var(--paper);
    font-weight: 900;
    font-size: 34px;
  }
  .contact-phone {
    position: absolute;
    left: 340px;
    top: 718px;
    display: flex;
    align-items: center;
    gap: 14px;
    color: var(--paper);
    font-weight: 700;
    font-size: 44px;
    line-height: 56px;
  }
  .contact-email {
    position: absolute;
    left: 342px;
    top: 774px;
    display: flex;
    align-items: center;
    gap: 14px;
    color: var(--paper);
    font-weight: 700;
    font-size: 25px;
    line-height: 32px;
  }
  .contact-address {
    position: absolute;
    left: 0;
    top: 820px;
    width: 1200px;
    text-align: center;
    color: var(--address-blue);
    font-weight: 700;
    font-size: 37px;
    line-height: 48px;
  }
</style>
</head>
<body>
<main class="postcard">
  <svg class="postcard-backdrop" width="1200" height="900" viewBox="0 0 1200 900" aria-hidden="true">
    <defs>
      <linearGradient id="swoosh" x1="0" y1="0" x2="1" y2="1">
        <stop offset="0" stop-color="#ffffff"/>
        <stop offset="0.5" stop-color="#e4e8f4"/>
        <stop offset="1" stop-color="#ffffff"/>
      </linearGradient>
    </defs>
    <rect width="1200" height="900" fill="url(#swoosh)"/>
    <path d="M0 0 H1200 V404 C1100 370 1000 260 820 215 C600 172 300 226 0 196 Z" fill="var(--brand-blue)"/>
    <path d="M0 684 H1200 V900 H0 Z" fill="var(--band-black)"/>
  </svg>

  <p class="tagline">We provide security guard services and we provide training for security guards.</p>

  <h2 class="services-tab">OUR SERVICES</h2>

  <ul class="service-list">
    <li>Armed and unarmed uninformed security guards</li>
    <li>Private detective</li>
    <li>Personal protection</li>
    <li>Background checks</li>
    <li>Marked vehicle patrols</li>
    <li>security consulting and risk assessment</li>
  </ul>

  <svg class="guard-photo" viewBox="0 0 570 646" role="img" aria-label="Photo of a security guard in a white shirt and sunglasses speaking into a handheld radio against a blue, cloudy sky">
    <defs>
      <linearGradient id="sky" x1="0" y1="0" x2="0.4" y2="1">
        <stop offset="0" stop-color="#6f95c6"/>
        <stop offset="0.35" stop-color="#b9cde4"/>
        <stop offset="0.7" stop-color="#eef1f5"/>
        <stop offset="1" stop-color="#d9dde3"/>
      </linearGradient>
    </defs>
    <path d="M9 9 H561 V450 C561 540 450 585 285 636 C120 585 9 540 9 450 Z" fill="url(#sky)" stroke="#ffffff" stroke-width="16"/>
  </svg>

  <div class="brand-block">
    <span class="brand-dot"></span>
    <span class="brand-name">Harbinger</span>
  </div>

  <p class="contact-phone">
    <svg width="34" height="34" viewBox="0 0 34 34" aria-hidden="true">
      <rect width="34" height="34" rx="6" fill="#ffffff"/>
      <path d="M11 7 C9 8 8 10 8.5 13 C10 20 15 25 21 26 C24 26.5 26 25 27 23 L23 19.5 L20.5 21.5 C17 20 14 17 12.5 13.5 L14.5 11 Z" fill="#050505"/>
    </svg>
    301-555-0142
  </p>
  <p class="contact-email">
    <svg width="32" height="22" viewBox="0 0 32 22" aria-hidden="true">
      <rect x="1" y="1" width="30" height="20" fill="none" stroke="#ffffff" stroke-width="2"/>
      <path d="M1 1 L16 13 L31 1" fill="none" stroke="#ffffff" stroke-width="2"/>
    </svg>
    service@harbinger2000.com.
  </p>
  <p class="contact-address">4120 Meridian Road, Suite 210, Glenwood Hills, MD 20790.</p>
</main>
</body>
</html>
```